2367 Halvorsen Avenue Medical Centre

We are looking for a design for new medical clinic.
We are accepting new patients at this new medical centre grand opening. Walk-ins are welcome.
Our cardiac and vascular surgical specialists are department heads at St Alder's Hospital, a leading teaching hospital in Toronto. These specialists will see cardiovascular consults are well as pre-surgical and post-surgical consultations and follow-ups.
Our lab is affiliated with several nuclear medicine clinics in the GTA.
Our Services Includes:
Family Practice
Cardiology Diagnostics
Cardiac & Vascular Surgical Consultation
Ultrasound & Vascular Testing
Open 6 days a week.
Ample Free Parking
Friendly Staffs

Target Market(s)

New Patients. Families of any age. Ethnic groups including Asians & Africans.

Industry/Entity Type

Medical

Font styles to use
Serif
Sans Serif
Decorative
Script
Other font styles liked:
• Arial calibri, verdana

Requirements
Must have
• Address:
• 2367 Halvorsen Avenue East
• Unit 225
• Scarborough, Ontario
• K7T 2P4
• Tel: (416) 555-0148
Nice to have
• Caring and inviting environment.
• Simple but classy.
• Standout colors.
Should not have
• Busy images. Aside from this, any ideas are welcome.

```html
<!DOCTYPE html>
<html lang="en">
<head>
<meta charset="utf-8">
<title>Halvorsen Avenue Medical Centre – Flyer</title>
<link href="https://fonts.googleapis.com/css2?family=Open+Sans:ital,wght@0,400;0,600;0,700;0,800;1,700;1,800&display=swap" rel="stylesheet">
<style>
  :root {
    --teal: #62c5b7;
    --teal-light: #a5e2d8;
    --teal-deep: #4fb3a5;
    --ink: #14302c;
    --band: #2a2a2a;
    --grey-1: #f4f4f4;
    --grey-2: #c9c9c9;
    --stage: #ffffff;
    --text: #1c1c1c;
  }
  * { box-sizing: border-box; margin: 0; padding: 0; }
  html, body {
    width: 1200px; height: 1200px; overflow: hidden;
    background: var(--stage);
    font-family: "Open Sans", Verdana, sans-serif;
    color: var(--text);
  }
  .flyer {
    position: absolute; left: 175px; top: 50px;
    width: 850px; height: 1100px;
    background: var(--teal);
    overflow: hidden;
    box-shadow: 0 6px 24px rgba(0,0,0,.18);
  }
  .flyer__waves { position: absolute; inset: 0; }
  .hero-photo {
    position: absolute; left: 62px; top: 20px;
    width: 330px; height: 330px; border-radius: 50%;
    border: 10px solid var(--band);
    background: radial-gradient(circle at 60% 55%, #f1f1ef 0%, #dcdfe2 40%, #7c9bb8 75%, #2f5f9c 100%);
    box-shadow: inset 0 0 0 6px #fff;
  }
  .brand {
    position: absolute; right: 40px; top: 95px;
    text-align: right;
    font-weight: 800; font-style: italic;
    font-size: 38px; line-height: 1.1;
    color: var(--ink);
  }
  .section-tab {
    position: absolute; left: 0;
    height: 44px; padding-right: 36px;
    display: flex; align-items: center; justify-content: flex-end;
    background: linear-gradient(90deg, rgba(98,197,183,0) 0%, var(--teal) 35%, var(--teal-light) 100%);
    font-weight: 800; font-style: italic; font-size: 25px; color: var(--ink);
    box-shadow: 0 6px 8px rgba(0,0,0,.12);
  }
  .section-tab--about { top: 385px; width: 330px; }
  .section-tab--team { top: 560px; width: 410px; }
  .section-copy {
    position: absolute; font-size: 16px; line-height: 1.3; text-align: justify;
    color: var(--text);
  }
  .section-copy--about { left: 70px; top: 445px; width: 360px; }
  .section-copy--team { left: 50px; top: 620px; width: 380px; }
  .services {
    position: absolute; left: 475px; top: 340px;
    width: 375px; height: 540px;
    background: linear-gradient(160deg, var(--teal-deep) 0%, var(--teal-light) 55%, var(--teal) 100%);
    padding: 40px 26px 0 30px;
    color: var(--ink);
  }
  .services__title { font-size: 46px; font-weight: 800; font-style: italic; line-height: 1; margin-bottom: 18px; }
  .services__list { list-style: none; font-size: 19px; line-height: 1.3; font-weight: 600; font-style: italic; }
  .services__list li { padding-left: 16px; position: relative; }
  .services__list li::before { content: "•"; position: absolute; left: 0; }
  .services__perks { margin-top: 36px; font-size: 22px; font-weight: 800; font-style: italic; line-height: 1.15; }
  .services__booking { margin-top: 38px; font-size: 21px; font-weight: 800; font-style: italic; line-height: 1.3; text-transform: uppercase; }
  .address {
    position: absolute; left: 40px; top: 1010px;
    display: flex; align-items: center; gap: 18px;
    font-size: 22px; font-style: italic; font-weight: 400; color: var(--text);
  }
  .address__icon { width: 26px; height: 26px; }
</style>
</head>
<body>
<main class="flyer">
  <svg class="flyer__waves" viewBox="0 0 850 1100" width="850" height="1100" aria-hidden="true">
    <defs>
      <linearGradient id="greyFill" x1="0" y1="0" x2="1" y2="1">
        <stop offset="0" stop-color="var(--grey-2)"/>
        <stop offset="0.45" stop-color="var(--grey-1)"/>
        <stop offset="1" stop-color="var(--grey-2)"/>
      </linearGradient>
    </defs>
    <path fill="var(--band)" d="M0,55 C300,150 500,225 850,262 L850,955 C500,905 200,910 0,835 Z"/>
    <path fill="url(#greyFill)" d="M0,92 C300,192 500,272 850,308 L850,905 C500,860 200,862 0,792 Z"/>
  </svg>

  <div class="hero-photo" role="img" aria-label="Photo of a nurse listening to an elderly patient's heart with a stethoscope"></div>

  <h1 class="brand">Halvorsen Avenue<br>Medical Centre</h1>

  <h2 class="section-tab section-tab--about">About Us</h2>
  <p class="section-copy section-copy--about">Halvorsen Avenue Medical Centre is a new medical clinic. We are accepting new patients at this new medical centre and accepting walk-in patients. Our lab is affiliated with several nuclear medicine clinics in the GTA.</p>

  <h2 class="section-tab section-tab--team">Our team of Experts</h2>
  <p class="section-copy section-copy--team">Our cardiac and vascular surgical specialists are department heads at St Alder's Hospital, a leading teaching hospital in Toronto. These specialists will see cardiovascular consults as well as pre-surgical and post-surgical consultations and follow-ups.</p>

  <section class="services">
    <h2 class="services__title">Our Services</h2>
    <ul class="services__list">
      <li>Family Practice</li>
      <li>Cardiology Diagnostics</li>
      <li>Cardiac &amp; Vascular Surgical Consultation</li>
      <li>Ultrasound &amp; Vascular</li>
    </ul>
    <p class="services__perks">Open 6 days a week.<br>Ample Free Parking<br>Friendly Staffs</p>
    <p class="services__booking">To book appointment,<br>please call (416) 555-0148</p>
  </section>

  <p class="address">
    <svg class="address__icon" viewBox="0 0 24 24" aria-hidden="true"><path fill="#111" d="M12 2 1 12h3v10h6v-6h4v6h6V12h3z"/></svg>
    2367 Halvorsen Avenue East, Unit 225, Scarborough, Ontario K7T 2P4
  </p>
</main>
</body>
</html>
```